Film Festival Poster Design Project

The 5th Annual Harrowgate Open Screen Festival will be taking place on November 12th in Wales at the Millbrook Picturehouse, Newport.

It is an all day event and there will be an eclectic mix of films on show.

Target Market(s)

Students 18-25

Industry/Entity Type

Festival

Requirements
Must have
• Title: 5th Harrowgate Open Screen Festival

Date: Saturday 12th November 2011

Place: Millbrook Playhouse & Picturehouse, Newport, Wales

Must include the text: BUY TICKETS ONLINE AT WWW.REELGATHERINGHUB.EXAMPLE

Sponsors & Festival Logo's must be included.
Nice to have
• As the festival is based in Wales, it would be nice to have a slightly Welsh tone to the poster, or a British feel.

```html
<!DOCTYPE html>
<html lang="en">
<head>
<meta charset="utf-8">
<title>Harrowgate Open Screen Festival – Reel Gathering Hub</title>
<link rel="stylesheet" href="https://fonts.googleapis.com/css2?family=Alfa+Slab+One&family=Libre+Baskerville:wght@400;700&family=Source+Sans+3:wght@400;600&display=swap">
<style>
  :root {
    --paper: #ffffff;
    --ink: #111111;
    --navy: #1f2c4c;
    --ticket-red: #ea4a5c;
    --ticket-frame: #b9b9b9;
    --tile-dark: #000000;
    --tile-light: #ffffff;
    --tile-line: #d8d8d8;
    --muted: #cfcfcf;
  }
  * { margin: 0; padding: 0; box-sizing: border-box; }
  html, body { width: 1200px; height: 900px; overflow: hidden; background: var(--paper); }
  .poster { position: relative; width: 1200px; height: 900px; background: var(--paper); color: var(--ink); font-family: "Source Sans 3", Arial, sans-serif; }

  .headline { position: absolute; left: 0; top: 0; width: 780px; height: 580px; }
  .headline text { font-family: "Alfa Slab One", Georgia, serif; fill: var(--ink); }

  .festival-name { position: absolute; left: 940px; top: 40px; width: 250px; font-family: "Source Sans 3", Arial, sans-serif; font-weight: 600; font-size: 26px; line-height: 1.25; color: var(--navy); }

  .ticket-button { position: absolute; left: 874px; top: 281px; width: 214px; height: 103px; background: var(--ticket-red); border: 4px solid var(--ticket-frame); display: flex; align-items: center; justify-content: center; text-align: center; font-family: "Libre Baskerville", Georgia, serif; color: var(--paper); font-size: 25px; line-height: 1.35; }

  .ticket-info { position: absolute; left: 800px; width: 368px; text-align: center; font-size: 20px; color: var(--ink); }
  .ticket-info.lead { top: 402px; }
  .ticket-info.url { top: 443px; }

  .event-details { position: absolute; left: 744px; top: 594px; font-size: 25px; line-height: 1.55; color: var(--ink); }
  .event-details .label { display: inline-block; width: 70px; }
  .event-details .indent { padding-left: 70px; display: block; }

  .sponsor-heading { position: absolute; left: 10px; top: 680px; font-family: "Libre Baskerville", Georgia, serif; font-weight: 700; font-size: 23px; letter-spacing: 0.5px; color: var(--ink); }

  .sponsor-row { position: absolute; left: 0; top: 728px; width: 1200px; height: 172px; }
  .sponsor { position: absolute; top: 0; height: 172px; display: flex; align-items: center; justify-content: center; font-family: "Source Sans 3", Arial, sans-serif; font-weight: 600; text-align: center; }
  .sponsor.dark { background: var(--tile-dark); color: var(--paper); }
  .sponsor.light { background: var(--tile-light); color: var(--ink); border: 2px solid var(--tile-line); }
  .sponsor-northlamp { left: 0; width: 281px; font-size: 28px; letter-spacing: 2px; }
  .sponsor-brightvale { left: 285px; width: 293px; font-size: 36px; letter-spacing: 3px; }
  .sponsor-kestrel { left: 585px; width: 315px; font-size: 28px; color: var(--muted); }
  .sponsor-harrowgate { left: 904px; width: 296px; font-size: 24px; line-height: 1.15; }
</style>
</head>
<body>
<main class="poster">

  <svg class="headline" viewBox="0 0 780 580" aria-label="Reel Gathering Hub">
    <text x="75" y="206" font-size="190" textLength="515" lengthAdjust="spacingAndGlyphs">REEL</text>
    <text x="19" y="385" font-size="170" textLength="731" lengthAdjust="spacingAndGlyphs">GATHERING</text>
    <text x="56" y="545" font-size="170" textLength="666" lengthAdjust="spacingAndGlyphs">HUB</text>
  </svg>

  <h1 class="festival-name">5th Harrowgate<br>Open Screen Festival</h1>

  <div class="ticket-button">BUY TICKETS<br>ONLINE</div>
  <p class="ticket-info lead">BUY TICKETS ONLINE AT</p>
  <p class="ticket-info url">WWW.REELGATHERINGHUB.EXAMPLE</p>

  <div class="event-details">
    <p><span class="label">Date:</span>Saturday 12th November 2011</p>
    <p><span class="label">Place:</span>Millbrook Playhouse &amp;</p>
    <p class="indent">Picturehouse, Newport, Wales</p>
  </div>

  <h2 class="sponsor-heading">SPONSERED BY</h2>

  <section class="sponsor-row">
    <div class="sponsor dark sponsor-northlamp">NORTHLAMP</div>
    <div class="sponsor light sponsor-brightvale">BRIGHTVALE</div>
    <div class="sponsor dark sponsor-kestrel">kestrel digital media</div>
    <div class="sponsor light sponsor-harrowgate">Harrowgate Open<br>Screen Festival</div>
  </section>

</main>
</body>
</html>
```